Design our letter, business card, powerpoint and more

We have a logo and want a design for our business use. Letters (word template), business card (for printing) powerpoint presentation (template) and more.

```html
<!DOCTYPE html>
<html lang="en">
<head>
<meta charset="utf-8">
<title>Veralon business card</title>
<link rel="stylesheet" href="https://fonts.googleapis.com/css2?family=Montserrat:wght@300;400;600;700&display=swap">
<style>
  :root {
    --backdrop: #e4e6e9;
    --card: #ffffff;
    --teal: #7cc3d9;
    --blue: #7d95d1;
    --grey-text: #9a9596;
    --brand-grey: #a19c9d;
    --soft-blue: #e3e9f5;
    --soft-teal: #e7f4f9;
  }
  * { box-sizing: border-box; margin: 0; padding: 0; }
  html, body {
    width: 1200px;
    height: 953px;
    overflow: hidden;
    background: var(--backdrop);
    font-family: "Montserrat", sans-serif;
  }
  .card {
    position: absolute;
    width: 560px;
    height: 320px;
    background: var(--card);
    box-shadow: 0 4px 14px rgba(0, 0, 0, 0.12);
    overflow: hidden;
  }
  .card--front { left: 60px; top: 150px; }
  .card--back { left: 590px; top: 500px; }

  .brand {
    position: absolute;
    display: flex;
    align-items: center;
    gap: 10px;
    color: var(--brand-grey);
    font-weight: 700;
    letter-spacing: 0.02em;
  }
  .brand__mark {
    background: var(--blue);
    flex: none;
  }
  .card--front .brand { right: 70px; top: 58px; font-size: 30px; }
  .card--front .brand__mark { width: 14px; height: 14px; }
  .card--back .brand {
    left: 50%; top: 50%;
    transform: translate(-50%, -50%);
    font-size: 52px;
  }
  .card--back .brand__mark { width: 22px; height: 22px; }

  .holder {
    position: absolute;
    left: 42px;
    top: 118px;
    z-index: 2;
  }
  .holder__name {
    font-size: 26px;
    line-height: 1.1;
    letter-spacing: 0.02em;
  }
  .holder__first { color: var(--teal); font-weight: 300; }
  .holder__last { color: var(--blue); font-weight: 600; }
  .holder__role {
    margin-top: 4px;
    font-size: 15px;
    color: var(--grey-text);
    font-weight: 400;
  }

  .contact {
    position: absolute;
    right: 34px;
    top: 160px;
    list-style: none;
    text-align: right;
    font-size: 13px;
    color: var(--grey-text);
    line-height: 1.55;
    z-index: 2;
  }
  .contact__item {
    display: flex;
    justify-content: flex-end;
    align-items: center;
    gap: 8px;
  }
  .contact__icon { width: 12px; height: 12px; flex: none; }
  .contact__address { margin-top: 8px; padding-right: 20px; }

  .decor {
    position: absolute;
    left: 90px;
    bottom: 0;
    width: 190px;
    height: 128px;
    z-index: 1;
    background: linear-gradient(180deg, rgba(227,233,245,0) 0%, var(--soft-blue) 45%, var(--soft-teal) 100%);
  }
</style>
</head>
<body>

<section class="card card--front" aria-label="Business card front">
  <div class="brand"><span class="brand__mark"></span>VERALON</div>

  <div class="holder">
    <p class="holder__name"><span class="holder__first">MARA</span> <span class="holder__last">LIND</span></p>
    <p class="holder__role">Director / CEO</p>
  </div>

  <ul class="contact">
    <li class="contact__item">(555) 204-3180
      <svg class="contact__icon" viewBox="0 0 12 12" aria-hidden="true"><path d="M3 1 L5 3 L4 4.5 Q5 7 7.5 8 L9 7 L11 9 L9.5 11 Q3 10 1 2.5 Z" fill="var(--blue)"/></svg>
    </li>
    <li class="contact__item">hello@veralon.com
      <svg class="contact__icon" viewBox="0 0 12 12" aria-hidden="true"><rect x="0.5" y="2.5" width="11" height="7" fill="var(--blue)"/><path d="M0.5 2.5 L6 6.5 L11.5 2.5" fill="none" stroke="#fff" stroke-width="1"/></svg>
    </li>
    <li class="contact__item">www.veralon.com
      <svg class="contact__icon" viewBox="0 0 12 12" aria-hidden="true"><circle cx="6" cy="6" r="5.3" fill="var(--blue)"/><path d="M0.7 6 H11.3 M6 0.7 V11.3 M6 0.7 Q2.5 6 6 11.3 M6 0.7 Q9.5 6 6 11.3" fill="none" stroke="#fff" stroke-width="0.7"/></svg>
    </li>
    <li class="contact__address">48 Harbor View Rd. Suite 210<br>Austin, TX 78701</li>
  </ul>

  <div class="decor" role="img" aria-label="Soft pale blue decorative backdrop area"></div>
</section>

<section class="card card--back" aria-label="Business card back">
  <div class="brand"><span class="brand__mark"></span>VERALON</div>
</section>

</body>
</html>
```